Women's Health - Hormone Imbalance, Menopause, Perimenopause.

We need a poster to match a letter that will be sent out. So people see the poster in store they are reminded about the letter and the newspaper ad.
The Poster is advertising a holistic approach to treating menopause, perimenopause and women's health in general specifically hormonal imbalance.
This it the writing required on the poster
"Are you feeling out of sorts? Is your body changing? Could it be your hormones?
If you’re experiencing changes due to hormonal imbalances, it’s important to consult with a qualified medical professional who understands your needs.
Karim Nasser, the uBlendwell Apothecary, can help. He has practiced pharmacy and nutritional medicine, helping people with hormone imbalances using a holistic approach for over 18 years.
Together, we look at issues around Hormonal Imbalance, Perimenopause and Menopause. To start, we take a profile of your sex hormones, Adrenals, Thyroids and Metabolic Pathways to see how we can best remedy the situation. Karim uses a holistic approach that treats you as a whole – not just the symptoms – for overall better wellness.
Want to know more? Karim is available for consultation on Wednesday Mornings at Red Gully Pharmacy and Thursday Mornings at Fernbrook Pharmacy.
SPECIAL OFFER! Make a booking for one session ($60) and get another session free! This limited-time package includes an initial consultation, historical hormone profile, follow-up consultation and wellness action plan.
To book an appointment with Karim, call 1300 462 851 today."
Pictures required to correspond with the writing. I've also uploaded my logo
Industry/Entity Type
Pharmacy
Font styles to use
Requirements
Must have
- Photos/Images to match the writing. Need women who are suffering from menopause with symptoms such as hot flashes, night sweats, anxiety, depression, fatigue, loss of libido, insomnia.
Nice to have
- Integrative Medicine, tailored medicine approach, Natural, approach, unique, tailor made solution

```html
<!DOCTYPE html>
<html lang="en">
<head>
<meta charset="utf-8">
<title>Hormone Health Poster – uBlendwell Apothecary</title>
<link href="https://fonts.googleapis.com/css2?family=Open+Sans:wght@300;400;700&family=Roboto+Condensed:wght@400;700&family=Roboto+Slab:wght@800&display=swap" rel="stylesheet">
<style>
  :root{
    --backdrop:#e9e9ea;
    --paper:#ffffff;
    --orange:#ee9a1d;
    --slate:#3b4150;
    --red:#b3232b;
    --yellow:#f3d41c;
    --navy:#174a6e;
    --teal:#124c70;
    --band-yellow:#f2e51e;
    --green:#a6c132;
    --purple-a:#8d42a6;
    --purple-b:#6c2f8d;
    --ink:#1d1d1f;
    --white:#ffffff;
  }
  html,body{margin:0;padding:0;width:1200px;height:1200px;overflow:hidden;background:var(--backdrop);}
  .poster{
    position:absolute;left:188px;top:21px;width:711px;height:998px;
    transform:scale(1.16);transform-origin:0 0;
    background:var(--paper);overflow:hidden;
    box-shadow:0 4px 16px rgba(0,0,0,.18);
    font-family:"Open Sans",sans-serif;color:var(--white);
  }
  .abs{position:absolute;}
  .headline-bubble{left:28px;top:26px;width:660px;height:95px;}
  .headline{left:28px;top:26px;width:660px;height:75px;margin:0;
    display:flex;align-items:center;justify-content:center;
    font-family:"Roboto Slab",serif;font-weight:800;font-size:38px;letter-spacing:-1px;color:var(--white);}
  .intro-panel{left:25px;top:101px;width:330px;height:312px;background:var(--slate);}
  .hero-photo{left:355px;top:101px;width:330px;height:312px;
    background:radial-gradient(ellipse at 60% 45%,#e6c9ad 0%,#d9b894 35%,#ece4da 75%,#f2eee9 100%);}
  .question{left:32px;width:320px;height:46px;border-radius:23px;background:var(--red);
    display:flex;align-items:center;justify-content:center;
    font-weight:300;font-size:25px;letter-spacing:-.5px;}
  .question b{color:var(--yellow);font-weight:700;}
  .q1{top:118px;}
  .q2{top:177px;}
  .intro-copy{left:25px;top:240px;width:330px;text-align:center;font-size:19px;line-height:30px;font-weight:300;letter-spacing:-.4px;}
  .intro-copy b{font-weight:700;}
  .intro-copy .hl{color:var(--yellow);font-weight:700;font-size:26px;}
  .rule{left:0;top:444px;width:711px;height:2px;background:var(--slate);}
  .ribbon-fold{top:436px;}
  .ribbon{left:37px;top:413px;width:640px;height:49px;background:var(--navy);
    display:flex;align-items:center;justify-content:center;text-align:center;
    font-family:"Roboto Condensed",sans-serif;font-size:13px;line-height:21px;}
  .ribbon b{font-weight:700;}
  .issues-lead{left:40px;top:476px;font-family:"Roboto Condensed",sans-serif;font-weight:700;font-size:14px;color:var(--navy);}
  .issues-band{left:0;top:499px;width:711px;height:224px;background:var(--teal);}
  .issue{position:absolute;top:4px;width:200px;text-align:center;}
  .issue-photo{width:164px;height:180px;border-radius:50%;margin:0 auto;}
  .issue-label{margin-top:10px;font-family:"Roboto Condensed",sans-serif;font-weight:700;font-size:15px;letter-spacing:.2px;}
  .issue-1{left:38px;} .issue-2{left:262px;} .issue-3{left:481px;}
  .ph-night{background:radial-gradient(circle at 60% 40%,#6a6e7a 0%,#2d313c 55%,#1a1c24 100%);}
  .ph-head{background:radial-gradient(circle at 50% 45%,#c8a18a 0%,#8d6650 45%,#eef0f2 100%);}
  .ph-meno{background:radial-gradient(circle at 50% 45%,#e0bfa3 0%,#c49a72 45%,#a48160 100%);}
  .profile-band{left:0;top:723px;width:711px;height:45px;background:var(--band-yellow);color:var(--ink);
    display:flex;align-items:center;justify-content:center;text-align:center;
    font-family:"Roboto Condensed",sans-serif;font-size:12.3px;line-height:15px;padding:0 18px;box-sizing:border-box;}
  .profile-band b{font-weight:700;}
  .contact-panel{left:0;top:768px;width:385px;height:178px;background:var(--slate);}
  .contact-title{left:0;top:771px;width:385px;text-align:center;font-size:22px;font-weight:400;}
  .contact-copy{left:0;top:808px;width:385px;text-align:center;font-size:14.5px;line-height:25px;}
  .contact-copy .y{color:var(--yellow);font-weight:700;}
  .contact-copy b{font-weight:700;}
  .brand{left:8px;top:896px;width:374px;height:46px;background:var(--white);
    display:flex;align-items:center;justify-content:center;gap:10px;
    font-family:"Open Sans",sans-serif;font-weight:700;font-size:22px;color:var(--navy);}
  .brand-dot{width:30px;height:30px;border-radius:50%;background:var(--navy);}
  .offer-tab{left:385px;top:768px;width:33px;height:178px;background:var(--green);border-top:2px solid var(--red);box-sizing:border-box;}
  .offer-tab span{position:absolute;left:50%;top:50%;transform:translate(-50%,-50%) rotate(-90deg);
    white-space:nowrap;font-family:"Roboto Condensed",sans-serif;font-weight:700;font-size:19px;color:var(--ink);letter-spacing:.5px;}
  .offer-panel{left:418px;top:768px;width:293px;height:178px;
    background:linear-gradient(180deg,var(--purple-a),var(--purple-b));border-top:2px solid var(--red);box-sizing:border-box;}
  .offer-head{left:418px;top:780px;width:293px;text-align:center;font-family:"Roboto Condensed",sans-serif;font-size:21px;line-height:32px;letter-spacing:-.3px;color:var(--yellow);}
  .offer-head .w{color:var(--white);font-weight:400;}
  .offer-head b{font-weight:700;}
  .offer-copy{left:418px;top:860px;width:293px;text-align:center;font-size:14.5px;line-height:18.5px;font-weight:400;}
  .cta-bar{left:0;top:946px;width:711px;height:44px;}
  .cta-text{left:22px;top:946px;height:44px;display:flex;align-items:center;
    font-family:"Roboto Condensed",sans-serif;font-weight:700;font-size:21px;}
  .cta-phone{left:480px;top:946px;height:44px;display:flex;align-items:center;gap:4px;
    font-family:"Roboto Condensed",sans-serif;font-weight:700;font-size:31px;}
</style>
</head>
<body>
<main class="poster">
  <svg class="abs headline-bubble" viewBox="0 0 660 95" width="660" height="95" aria-hidden="true">
    <rect x="0" y="0" width="660" height="75" rx="37.5" fill="var(--orange)"/>
    <polygon points="520,70 560,70 528,95" fill="var(--orange)"/>
  </svg>
  <h1 class="abs headline">Are you feeling out of sorts?</h1>

  <div class="abs intro-panel"></div>
  <div class="abs hero-photo" role="img" aria-label="Photo of a stressed woman holding her head in both hands"></div>

  <div class="abs question q1">Is your&nbsp;<b>body</b>&nbsp;<b style="color:var(--white)">changing ?</b></div>
  <div class="abs question q2">Could it be your&nbsp;<b>hormones ?</b></div>

  <p class="abs intro-copy" style="margin:0">
    If you’re experiencing <b>changes</b> due to<br>
    <span class="hl">hormonal imbalances,</span><br>
    it’s important to consult with a<br>
    <b>qualified medical professional</b><br>
    <b>who understands your needs.</b>
  </p>

  <div class="abs rule"></div>
  <svg class="abs ribbon-fold" style="left:18px" width="20" height="26" viewBox="0 0 20 26" aria-hidden="true"><polygon points="20,0 0,8 20,26" fill="var(--slate)"/></svg>
  <svg class="abs ribbon-fold" style="left:677px" width="20" height="26" viewBox="0 0 20 26" aria-hidden="true"><polygon points="0,0 20,8 0,26" fill="var(--slate)"/></svg>
  <div class="abs ribbon">
    <p style="margin:0"><b>Karim Nasser</b>, the <b>uBlendwell Apothecary</b>, can help. He has practiced <b>pharmacy</b> and <b>nutritional medicine</b>,<br>
    helping people with <b>hormone imbalances</b> using a <b>holistic approach</b> for <b>over 18 years</b>.</p>
  </div>

  <div class="abs issues-lead">Together, we look at issues around</div>
  <section class="abs issues-band">
    <div class="issue issue-1">
      <div class="issue-photo ph-night" role="img" aria-label="Photo of a sleepless woman in bed beside an alarm clock"></div>
      <div class="issue-label">HORMONAL IMBALANCE</div>
    </div>
    <div class="issue issue-2">
      <div class="issue-photo ph-head" role="img" aria-label="Photo of a young woman with a headache"></div>
      <div class="issue-label">PERIMENOPAUSE</div>
    </div>
    <div class="issue issue-3">
      <div class="issue-photo ph-meno" role="img" aria-label="Photo of a middle-aged woman touching her forehead"></div>
      <div class="issue-label">MENOPAUSE</div>
    </div>
  </section>

  <div class="abs profile-band">
    <p style="margin:0">To start, we take a profile of your <b>sex hormones</b>, <b>Adrenals</b>, <b>Thyroids</b> and <b>Metabolic Pathways</b> to see how we can best remedy the situation. Karim uses a holistic approach that treats you as a whole – not just the symptoms – for overall better wellness.</p>
  </div>

  <div class="abs contact-panel"></div>
  <h2 class="abs contact-title" style="margin:0">Want to know more?</h2>
  <p class="abs contact-copy" style="margin:0">
    <span class="y">Karim</span> is available for consultation on <span class="y">Wednesday</span><br>
    <span class="y">Mornings</span> at <b>Red Gully Pharmacy</b> and<br>
    <span class="y">Thursday Mornings</span> at <b>Fernbrook Pharmacy</b>.
  </p>
  <div class="abs brand"><span class="brand-dot"></span>uBlendwell Apothecary</div>

  <div class="abs offer-tab"><span>SPECIAL OFFER</span></div>
  <div class="abs offer-panel"></div>
  <p class="abs offer-head" style="margin:0">
    <b>BOOK FOR 1 SESSION</b> <span class="w">( $60) &amp;</span><br>
    <b>GET ANOTHER SESSION</b> <b style="color:#e6ef3a">FREE</b>
  </p>
  <p class="abs offer-copy" style="margin:0">This limited-time package includes an initial consultation, historical hormone profile, follow-up consultation and wellness action plan.</p>

  <svg class="abs cta-bar" viewBox="0 0 711 44" width="711" height="44" aria-hidden="true">
    <rect x="0" y="0" width="711" height="44" fill="var(--orange)"/>
    <polygon points="0,0 470,0 490,22 470,44 0,44" fill="#000"/>
  </svg>
  <div class="abs cta-text">To book an appointment with Karim, call today</div>
  <div class="abs cta-phone">
    <svg width="28" height="28" viewBox="0 0 28 28" aria-hidden="true">
      <circle cx="14" cy="14" r="12" fill="none" stroke="var(--red)" stroke-width="2.5"/>
      <path d="M9.5 8.5c1-1 2-.8 2.6.2l1 1.8c.4.8.2 1.5-.5 2l-.7.5c.6 1.4 1.7 2.6 3.1 3.2l.5-.7c.5-.7 1.3-.9 2-.5l1.8 1c1 .6 1.1 1.7.2 2.6-1.3 1.3-3.2 1.4-5.5-.2-2.4-1.7-4.5-4.2-5.1-6.5-.3-1.5 0-2.7.6-3.4z" fill="var(--red)"/>
    </svg>
    1300 462 851
  </div>
</main>
</body>
</html>
```